Mesh Banner Design for Business Premises

We require the design of a large mesh banner to be installed across the front fence of our warehouse. The banner should prominently feature our existing Trelborn logo and brand colours (yellow, white, and black) and be designed to be highly visible from the road.

The overall aesthetic should be strong, masculine, and industrial, reflecting the nature of the scaffolding and construction industry. The background should be predominantly black, with our branding incorporated in yellow and white for strong contrast and readability.

The banner should clearly communicate the full scope of services we provide, including:

Scaffold Design
Scaffold Engineering
Scaffold Installation / Erection
Scaffold Dismantling

It should also indicate the types of projects and clients we service, including:

Commercial
Industrial
Residential
Civil

The design should feel bold and professional, with a construction-oriented style that aligns with the scaffolding industry. It should be clean, impactful, and easy to read from a distance, ensuring passing traffic can quickly understand our services.

Where possible, subtle industrial or structural design elements (such as scaffold components, steel textures, or linework) may be incorporated into the background to reinforce the industry theme while keeping the layout uncluttered.

The final design will be produced as a large-format mesh banner for outdoor installation, so it should be created with this application and viewing distance in mind.

```html
<!DOCTYPE html>
<html lang="en">
<head>
<meta charset="utf-8">
<title>Trelborn Mesh Banner</title>
<link rel="stylesheet" href="https://fonts.googleapis.com/css2?family=Roboto+Condensed:wght@700&display=swap">
<style>
  :root {
    --black: #000000;
    --yellow: #f7b21b;
    --white: #ffffff;
    --silver-light: #e4e4e4;
    --silver-mid: #c9c9c9;
    --silver-dark: #a9a9a9;
    --wordmark: #c6c6c6;
    --ink: #0a0a0a;
  }
  html, body {
    margin: 0;
    padding: 0;
    width: 1200px;
    height: 300px;
    overflow: hidden;
    background: var(--black);
  }
  .banner {
    position: relative;
    width: 1200px;
    height: 300px;
    overflow: hidden;
    background: var(--black);
    font-family: "Roboto Condensed", "Arial Narrow", sans-serif;
    font-weight: 700;
  }
  .banner__backdrop {
    position: absolute;
    inset: 0;
  }
  .brand-name {
    position: absolute;
    left: 48px;
    top: 22px;
    margin: 0;
    font-size: 60px;
    line-height: 1;
    letter-spacing: 69px;
    color: var(--wordmark);
    text-transform: uppercase;
    white-space: nowrap;
  }
  .brand-mark {
    position: absolute;
    left: 90px;
    top: 100px;
    width: 150px;
    height: 150px;
    box-sizing: border-box;
    border: 5px solid var(--yellow);
  }
  .services {
    position: absolute;
    left: 323px;
    top: 92px;
    margin: 0;
    padding: 0;
    list-style: none;
  }
  .services__item {
    color: var(--white);
    font-size: 26px;
    line-height: 47px;
    height: 47px;
    text-transform: uppercase;
    white-space: nowrap;
  }
  .sectors {
    position: absolute;
    left: 889px;
    top: 34px;
    margin: 0;
    padding: 0;
    list-style: none;
  }
  .sectors__item {
    color: var(--ink);
    font-size: 44px;
    line-height: 61px;
    height: 61px;
    text-transform: uppercase;
    text-shadow: 1px 2px 2px rgba(0,0,0,0.35);
    white-space: nowrap;
  }
</style>
</head>
<body>
  <div class="banner">
    <svg class="banner__backdrop" width="1200" height="300" viewBox="0 0 1200 300" aria-hidden="true">
      <defs>
        <linearGradient id="brushed-steel" x1="0" y1="0" x2="1" y2="1">
          <stop offset="0" stop-color="var(--silver-dark)"/>
          <stop offset="0.35" stop-color="var(--silver-light)"/>
          <stop offset="0.7" stop-color="var(--silver-mid)"/>
          <stop offset="1" stop-color="var(--silver-light)"/>
        </linearGradient>
      </defs>
      <rect class="backdrop__black" x="0" y="0" width="1200" height="300" fill="var(--black)"/>
      <polygon class="backdrop__yellow-stripe" points="836,0 850,0 725,300 711,300" fill="var(--yellow)"/>
      <polygon class="backdrop__steel-stripe" points="857,0 862,0 737,300 732,300" fill="var(--silver-mid)"/>
      <polygon class="backdrop__steel-panel" points="870,0 1200,0 1200,300 745,300" fill="url(#brushed-steel)"/>
    </svg>

    <h1 class="brand-name">Trelborn</h1>
    <div class="brand-mark" aria-hidden="true"></div>

    <ul class="services">
      <li class="services__item">Scaffold Design</li>
      <li class="services__item">Scaffold Engineering</li>
      <li class="services__item">Scaffold Installation / Erection</li>
      <li class="services__item">Scaffold Dismantling</li>
    </ul>

    <ul class="sectors">
      <li class="sectors__item">Commercial</li>
      <li class="sectors__item">Industrial</li>
      <li class="sectors__item">Residential</li>
      <li class="sectors__item">Civil</li>
    </ul>
  </div>
</body>
</html>
```